Financial Service Company Need Business Card Design

This is a new startup company, first of its kind to offer this service. We facilitate the movement of deposit funds electronically between home buyers and real estate brokerages.Our customers are DOMIVANS®, real estate brokerages, and home buyers, we identify ourselves as a financial/technology company.
Not looking for anything too flashy. Just a clean design that shows the logo, contact info, etc. Company colors can be seen on attached logo, and 'coming soon page'
www.quorvanta.ca

```html
<!DOCTYPE html>
<html lang="en">
<head>
<meta charset="utf-8">
<title>Quorvanta Business Card</title>
<link rel="stylesheet" href="https://fonts.googleapis.com/css2?family=Encode+Sans+Semi+Condensed:wght@400;600&display=swap">
<style>
  :root {
    --backdrop: #f7f7f8;
    --card: #ffffff;
    --card-edge: #d9d9d9;
    --brand-orange: #e85120;
    --brand-tint: #f9dcd2;
    --ink: #666666;
  }
  html, body {
    margin: 0;
    padding: 0;
    width: 1200px;
    height: 1000px;
    overflow: hidden;
    background: var(--backdrop);
    font-family: "Encode Sans Semi Condensed", "Arial Narrow", sans-serif;
  }
  .canvas { position: relative; width: 1200px; height: 1000px; }
  .card {
    position: absolute;
    background: var(--card);
    border: 1px solid var(--card-edge);
    box-sizing: border-box;
    overflow: hidden;
  }
  .card-front { left: 370px; top: 157px; width: 456px; height: 279px; }
  .card-back  { left: 370px; top: 527px; width: 457px; height: 280px; }
  .card svg.art { position: absolute; left: 0; top: 0; }
  .brand-frame {
    position: absolute;
    left: 13px; top: 89px;
    width: 430px; height: 99px;
    box-sizing: border-box;
    border: 1px solid var(--brand-orange);
    border-radius: 14px;
    display: flex; align-items: center; justify-content: center;
  }
  .wordmark {
    display: flex; align-items: center; gap: 10px;
    color: var(--ink);
    font-weight: 600;
    letter-spacing: -0.3px;
  }
  .wordmark-square { background: var(--brand-orange); border-radius: 2px; }
  .brand-frame .wordmark { font-size: 31px; }
  .brand-frame .wordmark-square { width: 30px; height: 30px; }
  .card-back .wordmark {
    position: absolute; left: 28px; top: 50px;
    font-size: 27px;
  }
  .card-back .wordmark-square { width: 26px; height: 26px; }
  .contact-list {
    position: absolute; left: 30px; top: 137px;
    margin: 0; padding: 0; list-style: none;
    color: var(--ink); font-size: 15px; font-weight: 400;
  }
  .contact-list li { display: flex; align-items: center; height: 23px; }
  .contact-list svg { width: 17px; height: 17px; margin-right: 14px; flex: none; }
</style>
</head>
<body>
<div class="canvas">

  <section class="card card-front">
    <svg class="art" width="456" height="279" viewBox="0 0 456 279">
      <path d="M14 0 H440 L442 45 Q442 55 432 55 H24 Q14 55 14 45 Z" fill="var(--brand-orange)"/>
      <path d="M24 223 H432 Q442 223 442 233 L436 279 H19 L14 233 Q14 223 24 223 Z" fill="var(--brand-orange)"/>
    </svg>
    <div class="brand-frame">
      <div class="wordmark"><span class="wordmark-square"></span>Quorvanta</div>
    </div>
  </section>

  <section class="card card-back">
    <svg class="art" width="457" height="280" viewBox="0 0 457 280" role="img" aria-label="Soft tinted brand decoration">
      <polygon points="160,40 200,0 457,0 457,190 390,270 320,250" fill="var(--brand-tint)"/>
    </svg>
    <div class="wordmark"><span class="wordmark-square"></span>Quorvanta</div>
    <ul class="contact-list">
      <li>
        <svg viewBox="0 0 24 24"><path d="M3 9c0-3 4-4 9-4s9 1 9 4v2h-5V9H8v2H3z M6 12h12l2 7H4z" fill="var(--ink)"/><circle cx="12" cy="15.5" r="2" fill="#fff"/></svg>
        + 000 - 1234 - 5678
      </li>
      <li>
        <svg viewBox="0 0 24 24"><rect x="3" y="6" width="18" height="12" fill="none" stroke="var(--ink)" stroke-width="1.5"/><path d="M3 6l9 7 9-7" fill="none" stroke="var(--ink)" stroke-width="1.5"/></svg>
        admin@youremail.com
      </li>
      <li>
        <svg viewBox="0 0 24 24" fill="none" stroke="var(--ink)" stroke-width="1.4"><circle cx="12" cy="12" r="8.5"/><ellipse cx="12" cy="12" rx="3.8" ry="8.5"/><path d="M3.5 12h17M5 8h14M5 16h14"/></svg>
        www.quorvanta.ca
      </li>
      <li>
        <svg viewBox="0 0 24 24"><path d="M12 2a6.5 6.5 0 0 0-6.5 6.5C5.5 13.5 12 22 12 22s6.5-8.5 6.5-13.5A6.5 6.5 0 0 0 12 2z" fill="var(--ink)"/><circle cx="12" cy="8.5" r="2.4" fill="#fff"/></svg>
        777 Seventh Avenue, New York 54321
      </li>
    </ul>
  </section>

</div>
</body>
</html>
```